business card for Franco-Turkish restaurant

We are a Franco-Turkish restaurant, Le Mirandel, based in the Cotes d'Armor in Brittany, near the Pink Granite Coast. We serve mainly Turkish cuisine. We would like a card reminding Britain and Turkey. No flag. Color: turquoise (sea ..), green, red. There should be a space for 3 lines: name, address, phone / email

Industry/Entity Type

Fast Food Restaurant

Contact Information for Business Card

Dalbayrak Emrul
Addresse: 14 Rue Paul-Henri Duvic, 22450 Kervalhec, France
Tel:+33 2 96 47 08 39

Colors
33a6d7
f04a50
acd036

Requirements
Nice to have
• Symbols of Britain and Turkey
Should not have
• No flags

```html
<!DOCTYPE html>
<html lang="fr">
<head>
<meta charset="utf-8">
<title>Le Mirandel – carte de visite</title>
<link rel="stylesheet" href="https://fonts.googleapis.com/css2?family=Quicksand:wght@300;400&display=swap">
<style>
  :root {
    --sea: #55a3a8;
    --paper: #ffffff;
    --land-edge: #f4f7f7;
    --page: #ffffff;
    --shadow: rgba(0, 0, 0, 0.18);
  }
  html, body {
    margin: 0;
    padding: 0;
    width: 1200px;
    height: 1200px;
    overflow: hidden;
    background: var(--page);
  }
  .sheet {
    position: relative;
    width: 1200px;
    height: 1200px;
  }
  .card {
    position: absolute;
    top: 418px;
    width: 564px;
    height: 365px;
    background: var(--sea);
    overflow: hidden;
    box-shadow: 0 1px 3px var(--shadow);
    font-family: "Quicksand", sans-serif;
  }
  .card--front { left: 24px; }
  .card--back { left: 612px; }
  .card__land {
    position: absolute;
    background: linear-gradient(160deg, var(--paper) 0%, var(--land-edge) 100%);
  }
  .card--front .card__land {
    left: 70px;
    top: 170px;
    right: 0;
    bottom: 0;
  }
  .card--back .card__land {
    left: 0;
    top: 112px;
    right: 34px;
    bottom: 0;
  }
  .wordmark {
    position: absolute;
    left: 70px;
    top: 62px;
    margin: 0;
    font-family: "Quicksand", sans-serif;
    font-weight: 300;
    font-size: 50px;
    line-height: 1;
    color: var(--paper);
    letter-spacing: 1px;
    white-space: nowrap;
  }
  .contact {
    position: absolute;
    margin: 0;
    color: var(--sea);
    font-weight: 300;
    font-size: 18px;
    line-height: 20px;
    white-space: nowrap;
  }
  .contact--address {
    left: 47px;
    top: 208px;
    font-style: normal;
  }
  .contact--reach {
    right: 110px;
    top: 286px;
    text-align: right;
  }
  .contact--reach .phone { font-size: 19px; letter-spacing: 0.5px; }
</style>
</head>
<body>
<main class="sheet">

  <section class="card card--front" aria-label="Recto de la carte">
    <div class="card__land" role="img" aria-label="Emplacement de la carte du littoral breton en blanc"></div>
    <h1 class="wordmark">Le Mirandel</h1>
  </section>

  <section class="card card--back" aria-label="Verso de la carte">
    <div class="card__land" role="img" aria-label="Emplacement de la carte du littoral en blanc"></div>
    <h1 class="wordmark">Le Mirandel</h1>
    <address class="contact contact--address">
      14 Rue Paul-Henri Duvic<br>
      Face à la Halle et Place du Marché<br>
      22450 Kervalhec
    </address>
    <p class="contact contact--reach">
      <span class="phone">02 96 47 08 39</span><br>
      <span class="email">reservations@lemirandel.fr</span>
    </p>
  </section>

</main>
</body>
</html>
```